Tri-fold Brochure for a Massage Therapist Specializing in Injury Treatment

I need your help to make this brochure beautiful. It's 8 1/2" x 11", full color, two-sided, tri-fold.

It will be primarily distributed in medical clinics, so it should be visually attractive to people who are awaiting treatment for injuries sustained in a motor vehicle accident.

Motor vehicle accident claims are only one sub-section of my total clientele, so this is a specifically targeted campaign. However, I also have many clients that I see regularly as an ongoing part of their personal health and wellness regimen. These clients tend to have above-average incomes, and I would like this particular brochure to have some cross-over appeal to that market as well, if possible.

The plain text version of the two-sided design is attached. Both pages are already divided into thirds along the fold lines. Feel free to get creative with font sizing and spacing to accommodate graphics as long as the text within each folded section remains within that section.

I don't have an official logo, but I have been using the water droplet image (on the back of the brochure) on my web and print materials. It doesn't necessarily need to be included, but it would be nice for the sake of consistency. I'm attaching a copy of the droplet as well as a version that shows the style of font I've been using in other forms of print advertising.

Just FYI: I am a sole proprietor and my legal business name is my name - Marla J. Densford, LMP. "Gentle Tissue Care & Steady Recovery Massage" started out as more of a tag line, but has evolved into the non-official name of my business.

Thanks in advance for your help!

Target Market(s)

Women & men of all ages that have been injured in a motor vehicle accident.

Industry/Entity Type

Health Care

Font styles to use
Serif
Other font styles liked:
• KennedyCapsDB_Normal

Requirements
Must have
• Text content should remain as written. Brochure text within each folded section should remain within that section.
• I'm open to suggestions, though. And if you notice any typos, please let me know!
Nice to have
• Water drop image near my name on the back side would be nice to include, but it's not absolutely necessary.
• I personally prefer colors in shades of blue & green, but I look forward to seeing what the designers choose.
Should not have
• I am very particular about stock photos that represent massage therapy. I prefer photos that represent the way I work with my injured clients, so this excludes the strictly "spa-type" images such as beautiful half-naked women with flowers in their hair and warm stones placed along their spine.
• Also, I only do table massage; no chair massage. So stock photos showing patients seated in specially designed portable massage chairs should not be used.
• Photos should be more clinical in nature, not picture the therapist other than their arms & hands (which should be female), and not picture the patient's exposed hips or side of the breast. All draping of the patient's body (male or female) must be complete & secure - no towels, tube tops, or bikinis.
• I would prefer that any photos of the therapist's hands look similar to mine, which are female, petite, and fair skinned without freckles. The skin tone of the pictured patient does not matter.
• If the patient is pictured face down, they need to be using the table's face cradle, not with their head turned to either side. (Anyone with whiplash would look at a photo like that and just see pain!) Likewise, the therapist's action should not look painful, so no photos of deep tissue techniques involving knuckles, elbows, or uncomfortable body positioning.
• The majority of my injured patients have lower back, upper back, neck and shoulder pain, so pictures that feature these areas (in the way I've outlined above) would be preferred.
• If you have any questions about photos, please don't hesitate to ask!

```html
<!DOCTYPE html>
<html lang="en">
<head>
<meta charset="utf-8">
<title>Injury Massage Brochure – Inside Spread</title>
<link href="https://fonts.googleapis.com/css2?family=Gelasio:ital,wght@0,400;0,700;1,400;1,700&display=swap" rel="stylesheet">
<style>
  :root {
    --page-bg: #d9d9d9;
    --sky: #2ea3dc;
    --sky-deep: #1b86c6;
    --navy: #1f5f93;
    --navy-dark: #17456f;
    --ink-blue: #1d5a8f;
    --text-dark: #1c2a3a;
    --paper: #ffffff;
    --mist: #e8f0f6;
    --photo-skin: #e9d2c2;
    --photo-cloth: #f1f3f5;
    --photo-green: #cfe0d2;
  }
  * { box-sizing: border-box; margin: 0; padding: 0; }
  html, body { width: 1200px; height: 960px; overflow: hidden; background: var(--page-bg); }
  body { font-family: "Gelasio", Georgia, serif; }

  .brochure {
    position: absolute; left: 30px; top: 39px;
    width: 1140px; height: 882px;
    display: flex; background: var(--paper);
  }
  .panel { position: relative; width: 380px; height: 100%; overflow: hidden; }

  /* Left panel */
  .panel--accident { background: var(--paper); }
  .accident__body {
    position: absolute; left: 0; top: 0; width: 100%; height: 566px;
    background: linear-gradient(160deg, #47b6e8 0%, var(--sky) 45%, var(--sky-deep) 100%);
    color: #fff; padding: 26px 26px 0 28px;
    font-size: 11.4px; line-height: 14.6px;
  }
  .accident__body p { margin-bottom: 9px; }
  .accident__body strong { font-weight: 700; }
  .accident__rule { position: absolute; left: 0; top: 566px; width: 100%; height: 8px; background: var(--navy); }
  .accident__photo {
    position: absolute; left: 0; top: 574px; width: 100%; height: 308px;
    background: linear-gradient(120deg, var(--photo-cloth) 0%, #e4e8ec 55%, var(--photo-skin) 100%);
  }

  /* Middle panel */
  .panel--therapy { background: linear-gradient(180deg, #fff 0%, #f3f6f9 100%); }
  .therapy__band { position: absolute; left: 0; top: 0; width: 100%; height: 58px; }
  .therapy__title {
    position: absolute; left: 24px; top: 12px;
    font-style: italic; font-weight: 700; font-size: 24px; color: #fff;
  }
  .therapy__photo {
    position: absolute; left: 0; top: 58px; width: 100%; height: 132px;
    background: linear-gradient(100deg, var(--navy-dark) 0%, #c9b3a6 30%, var(--photo-skin) 60%, #f4f4f4 100%);
  }
  .therapy__text {
    position: absolute; left: 30px; top: 214px; width: 326px;
    font-style: italic; font-size: 11.8px; line-height: 15.4px; color: var(--ink-blue);
  }
  .therapy__text p { margin-bottom: 11px; }
  .benefits { list-style: none; margin-left: 12px; }
  .benefits li { font-weight: 700; font-size: 12.2px; margin-bottom: 9.5px; }
  .benefits li::before { content: "•"; margin-right: 8px; }
  .therapy__curve { position: absolute; left: 0; bottom: 0; width: 100%; height: 130px; }

  /* Right panel */
  .panel--about { background: linear-gradient(180deg, #fff 0%, #f2f6fa 40%, var(--mist) 100%); }
  .about__band { position: absolute; left: 0; top: 0; width: 100%; height: 130px; }
  .about__portrait {
    position: absolute; left: 22px; top: 18px; width: 96px; height: 96px; border-radius: 50%;
    border: 4px solid var(--navy-dark);
    background: radial-gradient(circle at 50% 40%, #b77a5c 0%, #8a5a40 45%, #6f8f5a 100%);
  }
  .about__name {
    position: absolute; left: 132px; top: 86px;
    font-size: 19px; color: #fff; letter-spacing: 0.3px;
  }
  .about__name small { font-size: 12px; }
  .about__text {
    position: absolute; left: 24px; top: 146px; width: 334px;
    font-size: 12.8px; line-height: 16.2px; color: var(--text-dark);
  }
  .about__text p { margin-bottom: 10px; }
  .about__photo { position: absolute; left: 0; bottom: 0; width: 100%; height: 300px; }
</style>
</head>
<body>
<main class="brochure">

  <section class="panel panel--accident">
    <div class="accident__body">
      <p>According to the automotive insurance industry's statistics, more than 2 million people are injured in car accidents every year.</p>
      <p>If you are one of these people, you may be surprised to know that the Personal Injury Protection (PIP) coverage of your auto insurance policy will pay for you to receive massage therapy for your injuries. Why? Insurance companies know that <strong>massage therapy reduces pain and shortens the total recovery time after an injury.</strong></p>
      <p>In an instant, a collision can cause profound damage to your musculoskeletal system, and the results are not always immediately felt. Thanks to your body's natural defense mechanisms – including an immediate rush of adrenaline – you might not feel the effects of the impact until the shock wears off and your body begins to process the damage. Hours, days, weeks, or even months may pass before the full effects are realized.</p>
      <p><strong>A minor accident can have a major impact on your health for years to come.</strong> In fact, an impact at just 5 mph can be enough to cause a whiplash injury, chronic headaches, sciatica, and significant bodily pain, particularly in the back, shoulder, knee, or hip, in addition to a host of other potential health issues.</p>
      <p>If you or someone you care about has been involved in a motor vehicle accident, the first step on the path to optimal wellness is a visit to a physician for an examination and prescription for massage therapy.</p>
    </div>
    <div class="accident__rule"></div>
    <div class="accident__photo" role="img" aria-label="Photo of a person in white clothing holding their lower back in pain"></div>
  </section>

  <section class="panel panel--therapy">
    <svg class="therapy__band" viewBox="0 0 380 58" preserveAspectRatio="none" aria-hidden="true">
      <rect width="380" height="58" fill="var(--navy)"/>
      <path d="M0 46 Q190 34 380 40 L380 58 L0 58 Z" fill="var(--sky)"/>
    </svg>
    <h2 class="therapy__title">Effective Therapy</h2>
    <div class="therapy__photo" role="img" aria-label="Photo of a therapist's hands massaging a client's draped lower back"></div>
    <div class="therapy__text">
      <p>Massage therapy is well known for its ability to promote a deep sense of relaxation. However, the benefits extend far beyond simply feeling relaxed. Multiple research studies have conclusively proven the positive health benefits of therapeutic massage, particularly its effectiveness for injury rehabilitation.</p>
      <p>One recent study at Northbrook University found that just 10 minutes of massage therapy not only caused a reduction in muscle tension and pain, but also triggered a biochemical response that reduced inflammation and promoted cellular repair in damaged muscle tissue, speeding the healing process.</p>
      <p>Therapeutic massage has been proven to aid rehabilitation by:</p>
      <ul class="benefits">
        <li>Reducing pain</li>
        <li>Reducing stress &amp; muscle tension</li>
        <li>Relieving muscle spasms</li>
        <li>Reducing frequency &amp; duration of headaches</li>
        <li>Improving flexibility &amp; range of motion in joints</li>
        <li>Decreasing swelling &amp; improving circulation</li>
        <li>Enhancing quality of sleep</li>
        <li>Decreasing anxiety &amp; depression</li>
        <li>Shortening recovery time</li>
      </ul>
    </div>
    <svg class="therapy__curve" viewBox="0 0 380 130" preserveAspectRatio="none" aria-hidden="true">
      <path d="M200 130 Q270 40 380 22 L380 130 Z" fill="#dfe9f1"/>
      <path d="M240 130 Q300 50 380 36" fill="none" stroke="var(--sky)" stroke-width="10"/>
    </svg>
  </section>

  <section class="panel panel--about">
    <svg class="about__band" viewBox="0 0 380 130" preserveAspectRatio="none" aria-hidden="true">
      <rect width="380" height="120" fill="var(--navy-dark)"/>
      <path d="M0 0 L380 0 L380 20 Q200 10 0 30 Z" fill="var(--navy)"/>
      <path d="M0 120 L380 120 L380 130 L0 130 Z" fill="var(--sky)"/>
    </svg>
    <div class="about__portrait" role="img" aria-label="Portrait photo of the massage therapist"></div>
    <h1 class="about__name">Marla J. Densford, <small>LMP</small></h1>
    <div class="about__text">
      <p>Since my initial certification as a Licensed Massage Practitioner in 1997, I've continued to pursue advanced training in multiple bodywork modalities, including Myofascial Release, Neuromuscular Therapy, Manual Lymphatic Drainage, injury-specific deep tissue techniques, and many more.</p>
      <p>In my private practice I've had the opportunity to work with people of all ages, from infants to seniors, in a variety of settings from upscale spas and health clubs to medical clinics and rehabilitation centers. All of this has influenced my unique bodywork style.</p>
      <p>Multiple techniques are incorporated into each massage session, determined by the specific injuries involved, as well as your personal preferences and treatment goals. I believe very strongly that effective treatment work should also be as relaxing as possible, and I strive to combine the science of a clinically-focused therapeutic approach with the flowing artistry of a soothing spa experience – all in the comfort of your own home or office.</p>
      <p>My ultimate goal is to leave you feeling more relaxed, balanced, and rejuvenated, with a deeper understanding of your own body. It is in this state that the most profound healing can occur.</p>
    </div>
    <svg class="about__photo" viewBox="0 0 380 300" preserveAspectRatio="none" role="img" aria-label="Photo of a therapist's hands working on a client's lower leg and foot">
      <defs>
        <linearGradient id="legPhoto" x1="0" y1="0" x2="1" y2="1">
          <stop offset="0" stop-color="var(--photo-green)"/>
          <stop offset="0.45" stop-color="var(--photo-skin)"/>
          <stop offset="1" stop-color="#f4f6f8"/>
        </linearGradient>
      </defs>
      <path d="M0 40 Q190 -10 380 60 L380 300 L0 300 Z" fill="url(#legPhoto)"/>
      <path d="M0 40 Q190 -10 380 60" fill="none" stroke="var(--navy)" stroke-width="8"/>
    </svg>
  </section>

</main>
</body>
</html>
```